Software company seeking fresh website design

Using an already existing logo create a fresh, clean and professional web design for our company "Byte Lantern". Byte Lantern focuses on making business better through system integrations and software product development.

We're looking for a web design which has layouts for the following pages:
- Home Page
- Team Page
- Case Studies
- Market (List of Products)
- Product Page (Individual Product Details)
- About Page
- Media Page

Some websites and designs we'd like you to take inspiration from:
- Quillor.com
- https://www.portfolux.net/gallery/71830256/Taskly-redesign
- https://pixelnook.com/shots/5817362-Full-Range-Website-Design-for-a-Software-Company

Ideally the design should communicate an enterprise-level business with years of experience that can be trusted to deliver on budget and on-time.

Target Market(s)

Medium to High-Level Enterprise

Industry/Entity Type

Software Development

Coding

Coded - Design and coding required

Number of Pages Required

5+ page

Font styles to use
Sans Serif

Colors

Designer to choose colors to be used in the design.

Requirements
Must have
• - High Level of Professionalism
• - Be a unique design
• - Come with well-formatted and organised html + css + javascript
• - Must work on ie9, latest Chrome, latest Firefox, latest safari. iPhone6 and Android
• - Must be a progressive template
• - Must incorporate logo colors or at least be compatible with them
Nice to have
• - Hero, an area to display things we're proud of but look good without that area if need be.
• - Juicy animations that are performant and degrade nicely
Should not have
• - Submission must not be a template re-branded for the business

```html
<!DOCTYPE html>
<html lang="en">
<head>
<meta charset="utf-8">
<title>Byte Lantern Co. — Accelerating Enterprise Innovation</title>
<link href="https://fonts.googleapis.com/css2?family=Montserrat:wght@400;500;600;700;800&family=Open+Sans:wght@400;600;700&display=swap" rel="stylesheet">
<style>
:root{
  --orange:#f15a24;
  --orange-2:#f7931e;
  --orange-soft:#fff3ec;
  --ink:#2e2e2e;
  --muted:#7a7a7a;
  --line:#e6e6e6;
  --dark:#262626;
  --white:#ffffff;
  --blue:#2d7fd3;
  --footer:#f8f8f8;
}
*{box-sizing:border-box;margin:0;padding:0}
html,body{width:1200px;height:4696px;overflow:hidden}
body{position:relative;background:var(--white);font-family:"Open Sans",Arial,sans-serif;color:var(--ink)}
.abs{position:absolute}
h1,h2,h3,h4{font-family:"Montserrat",Arial,sans-serif}
.section-title{font-size:38px;font-weight:700;text-align:center;color:var(--ink)}
.section-title .accent{color:var(--orange)}
.lead{font-size:13px;line-height:22px;color:var(--muted);text-align:center}
.btn{display:inline-flex;align-items:center;position:relative;height:26px;padding:0 40px 0 20px;background:var(--orange);color:var(--white);border-radius:13px;font-family:"Montserrat",Arial,sans-serif;font-size:10px;font-weight:700;letter-spacing:.5px;text-transform:uppercase}
.btn::after{content:"";position:absolute;right:-6px;top:7px;width:30px;height:14px;background:var(--dark);border-radius:2px 10px 10px 2px;transform:skewX(-20deg)}
.btn.light{background:var(--white);color:var(--orange)}

/* header */
.logo{left:130px;top:34px;display:flex;align-items:center;gap:8px;font-family:"Montserrat",Arial,sans-serif;font-weight:700;font-size:22px;color:var(--orange)}
.logo .dot{width:14px;height:14px;border-radius:50%;background:var(--orange)}
.menu-toggle{left:1012px;top:22px;width:40px;height:40px;border-radius:50%;border:2px solid var(--white);display:flex;flex-direction:column;align-items:center;justify-content:center;gap:4px}
.menu-toggle span{width:16px;height:2px;background:var(--white)}

/* hero */
.hero-title{left:140px;top:214px;font-size:31px;font-weight:700;color:var(--ink)}
.hero-sub{left:140px;top:262px;font-size:24px;font-weight:500;color:var(--ink);font-family:"Montserrat",Arial,sans-serif}
.hero-actions{left:140px;top:322px;display:flex;gap:28px}

/* about */
.about-title{left:0;top:596px;width:1200px}
.about-text{left:240px;top:672px;width:720px}
.about-btn{left:520px;top:780px}

/* services */
.services-title{left:0;top:1020px;width:1200px}
.services-lead{left:280px;top:1086px;width:640px}
.service-grid{left:140px;top:1170px;width:920px;display:grid;grid-template-columns:repeat(4,200px);gap:40px 40px}
.service-card{height:150px;background:var(--white);border-radius:4px;box-shadow:0 4px 18px rgba(0,0,0,.08);display:flex;flex-direction:column;align-items:center;padding:26px 18px 0;text-align:center}
.service-card.featured{border:1px solid var(--orange);background:var(--orange-soft)}
.service-card svg{width:34px;height:34px;margin-bottom:14px}
.service-card h4{font-size:11px;font-weight:700;line-height:16px;color:var(--ink)}
.service-card.featured h4{color:var(--orange)}
.services-btn{left:532px;top:1594px}

/* products */
.products-title{left:140px;top:1850px;font-size:38px;font-weight:700}
.products-title .accent{color:var(--orange)}
.products-text{left:140px;top:1910px;width:400px;font-size:13px;line-height:22px;color:var(--muted)}
.products-btn{left:140px;top:2140px}
.product-card{left:660px;top:1830px;width:440px;height:400px;background:var(--white);border-radius:6px;box-shadow:0 10px 40px rgba(0,0,0,.12);padding:44px 40px}
.product-card h3{font-size:22px;font-weight:700;color:var(--orange);margin-bottom:22px}
.product-card p{font-size:13px;line-height:23px;color:var(--muted)}
.product-card .more{margin-top:30px;font-family:"Montserrat",Arial,sans-serif;font-size:11px;font-weight:700;color:var(--orange);letter-spacing:.5px}
.pager{position:absolute;right:36px;top:48px;display:flex;gap:6px}
.pager span{width:0;height:0;border-top:6px solid transparent;border-bottom:6px solid transparent}
.pager .prev{border-right:8px solid var(--orange)}
.pager .next{border-left:8px solid var(--dark)}

/* team */
.team-title{left:0;top:2432px;width:1200px}
.team-lead{left:300px;top:2500px;width:600px}
.avatar{border-radius:50%;background:linear-gradient(135deg,#d9c3b0,#8a7668)}
.avatar.main{border:6px solid var(--white);box-shadow:0 0 0 4px var(--orange)}
.member-name{left:0;top:2870px;width:1240px;text-align:center;font-family:"Montserrat",Arial,sans-serif;font-size:15px;font-weight:700}
.member-role{left:0;top:2894px;width:1240px;text-align:center;font-size:11px;color:var(--muted)}
.member-social{left:578px;top:2924px;display:flex;gap:12px}
.member-social span{width:22px;height:22px;border-radius:50%;border:1px solid var(--orange)}
.member-social span.on{background:var(--orange)}

/* case studies */
.case-card{left:120px;top:3236px;width:440px;height:360px;background:var(--white);border-radius:6px;box-shadow:0 10px 40px rgba(0,0,0,.14);padding:44px 40px}
.case-card h3{font-size:20px;font-weight:700;color:var(--ink);margin-bottom:20px}
.case-card p{font-size:13px;line-height:23px;color:var(--muted)}
.case-card .more{margin-top:26px;font-family:"Montserrat",Arial,sans-serif;font-size:11px;font-weight:700;color:var(--orange)}
.case-title{left:620px;top:3262px;font-size:38px;font-weight:700;color:var(--ink)}
.case-title .accent{color:var(--orange)}
.case-text{left:620px;top:3326px;width:440px;font-size:13px;line-height:22px;color:var(--muted)}
.case-btn{left:620px;top:3416px}

/* cta */
.cta-title{left:0;top:3766px;width:1200px;font-size:38px;font-weight:800;text-align:center;color:var(--ink)}
.cta-title .accent{color:var(--orange)}
.cta-btn{left:524px;top:3850px}

/* tech partners */
.tech-row{left:140px;width:920px;display:flex;justify-content:space-between;align-items:center}
.tech{display:flex;align-items:center;gap:10px;font-family:"Montserrat",Arial,sans-serif;font-weight:600;font-size:26px;color:#8c8c8c}
.tech i{display:block;width:26px;height:26px;border-radius:50%;background:#a8a8a8}

/* footer */
.footer{left:0;top:4280px;width:1200px;height:380px;background:var(--footer)}
.footer-col{top:4330px}
.footer-col h4{font-size:15px;font-weight:700;color:var(--ink);margin-bottom:22px}
.footer-col h4 .accent{color:var(--orange)}
.links li{list-style:none;font-size:12px;color:var(--muted);line-height:26px;padding-left:14px;position:relative}
.links li::before{content:"";position:absolute;left:0;top:12px;width:4px;height:4px;border-radius:50%;background:var(--orange)}
.contact .brand{font-family:"Montserrat",Arial,sans-serif;font-size:14px;font-weight:700;color:var(--orange);margin-bottom:14px}
.contact .row{display:flex;gap:10px;font-size:12px;color:var(--muted);line-height:19px;margin-bottom:12px}
.contact svg{flex:none;width:14px;height:14px;margin-top:3px}
.inquiry .field{width:220px;height:28px;border:1px solid var(--line);background:var(--white);margin-bottom:8px;font-size:11px;color:#aaa;padding:6px 10px}
.inquiry .field.tall{height:52px}
.follow li{list-style:none;display:flex;align-items:center;gap:12px;font-size:12px;color:var(--muted);margin-bottom:14px}
.follow li span{width:24px;height:24px;border-radius:50%;background:var(--blue)}
.copyright{left:0;top:4660px;width:1200px;height:36px;background:var(--dark);color:#bdbdbd;font-size:11px;display:flex;align-items:center;justify-content:center}
</style>
</head>
<body>

<!-- decorative background waves -->
<svg class="abs" style="left:0;top:0" width="1200" height="4696" viewBox="0 0 1200 4696" aria-hidden="true">
  <defs>
    <linearGradient id="orangeGrad" x1="0" y1="0" x2="1" y2="1">
      <stop offset="0" stop-color="#f7931e"/>
      <stop offset="1" stop-color="#f15a24"/>
    </linearGradient>
  </defs>
  <path d="M0 440 C300 500 500 420 700 480 C900 540 1050 500 1200 460 L1200 620 C1000 660 700 560 400 600 C200 630 80 580 0 560Z" fill="#fdf4ee"/>
  <path d="M0 1700 C300 1660 600 1740 1200 1660 L1200 1720 C800 1780 300 1720 0 1760Z" fill="#fdf4ee"/>
  <!-- hero blob -->
  <path d="M600 0 L1200 0 L1200 470 C1120 520 1040 440 960 470 C880 500 820 560 740 520 C660 480 700 400 640 360 C580 320 560 240 600 180 C640 120 560 60 600 0Z" fill="url(#orangeGrad)"/>
  <circle cx="1060" cy="520" r="26" fill="#f15a24"/>
  <circle cx="1110" cy="480" r="14" fill="#f7931e"/>
  <!-- products blob -->
  <path d="M560 1760 C700 1740 900 1700 1200 1730 L1200 2300 C1080 2340 980 2260 880 2300 C780 2340 680 2360 600 2300 C520 2240 560 2140 520 2060 C480 1980 470 1800 560 1760Z" fill="url(#orangeGrad)"/>
  <!-- case studies blob -->
  <path d="M0 3130 C140 3110 260 3150 380 3130 C520 3110 640 3180 620 3300 C600 3420 660 3520 600 3620 C540 3720 400 3760 260 3740 C140 3720 60 3770 0 3760Z" fill="url(#orangeGrad)"/>
</svg>

<!-- header -->
<div class="abs logo"><span class="dot"></span>Byte Lantern</div>
<div class="abs menu-toggle" aria-label="Menu"><span></span><span></span><span></span></div>

<!-- hero -->
<div class="abs" role="img" aria-label="Illustration of a team building a website on a large monitor" style="left:700px;top:60px;width:420px;height:380px;border-radius:24px;background:linear-gradient(160deg,#fde3d2 0%,#f8b98f 55%,#e9e9ef 100%);opacity:.92"></div>
<h1 class="abs hero-title">Accelerating Enterprise Innovation</h1>
<p class="abs hero-sub">Through Proven Strategic Initiatives</p>
<div class="abs hero-actions"><span class="btn">Learn More</span><span class="btn">Free Quote</span></div>

<!-- about -->
<h2 class="abs section-title about-title">About <span class="accent">Byte Lantern Co.</span></h2>
<p class="abs lead about-text">Byte Lantern Co. was originally founded as a small studio and has since grown into a trusted enterprise partner. For years we have helped companies modernise their systems, combining deep integration skills with product thinking, so teams can launch faster, scale safely and deliver every project on budget and on time.</p>
<div class="abs about-btn"><span class="btn">Read More</span></div>

<!-- services -->
<h2 class="abs section-title services-title"><span class="accent">Our</span> Services</h2>
<p class="abs lead services-lead">Byte Lantern focuses on making business better through integration, helping businesses keep pace with the changing landscape of the digital economy.</p>
<div class="abs service-grid">
  <div class="service-card"><svg viewBox="0 0 34 34" fill="none" stroke="#f15a24" stroke-width="2"><path d="M17 4 L28 10 L28 24 L17 30 L6 24 L6 10Z"/><path d="M17 12 v10 M12 17 h10"/></svg><h4>Enterprise Accelerator</h4></div>
  <div class="service-card featured"><svg viewBox="0 0 34 34" fill="none" stroke="#f15a24" stroke-width="2"><path d="M6 28 h22 M10 28 v-10 l7-8 7 8 v10"/><rect x="14" y="20" width="6" height="8"/></svg><h4>Minimum Viable Product Development &amp; Delivery</h4></div>
  <div class="service-card"><svg viewBox="0 0 34 34" fill="none" stroke="#f15a24" stroke-width="2"><path d="M17 5 a8 8 0 0 1 5 14 v4 h-10 v-4 a8 8 0 0 1 5-14Z"/><path d="M13 27 h8"/></svg><h4>Ideation &amp; Innovation Workshops</h4></div>
  <div class="service-card"><svg viewBox="0 0 34 34" fill="none" stroke="#f15a24" stroke-width="2"><rect x="5" y="8" width="24" height="18" rx="2"/><path d="M12 14 l-3 3 3 3 M22 14 l3 3-3 3"/></svg><h4>Contractual Developer Services on Demand</h4></div>
  <div class="service-card"><svg viewBox="0 0 34 34" fill="none" stroke="#f15a24" stroke-width="2"><rect x="11" y="4" width="12" height="26" rx="2"/><path d="M15 26 h4"/></svg><h4>Mobile &amp; Web Application Development</h4></div>
  <div class="service-card"><svg viewBox="0 0 34 34" fill="none" stroke="#f15a24" stroke-width="2"><path d="M6 28 V18 M13 28 V12 M20 28 V16 M27 28 V6"/></svg><h4>Application Scalability and Sustainability Consultation</h4></div>
  <div class="service-card"><svg viewBox="0 0 34 34" fill="none" stroke="#f15a24" stroke-width="2"><circle cx="17" cy="17" r="12"/><path d="M17 10 v7 l5 3"/></svg><h4>24/7 Emergency Scalability &amp; Site Support</h4></div>
  <div class="service-card"><svg viewBox="0 0 34 34" fill="none" stroke="#f15a24" stroke-width="2"><path d="M5 26 l8-8 5 5 11-12"/><path d="M22 11 h7 v7"/></svg><h4>Help your business succeed in the digital economy</h4></div>
</div>
<div class="abs services-btn"><span class="btn">Learn More</span></div>

<!-- products -->
<h2 class="abs products-title"><span class="accent">Our</span> Products</h2>
<p class="abs products-text">At Byte Lantern Co. we don't just prescribe solutions for every business. As a software company we build products of our own, shaped by what we learn in the field, so clients gain proven tools that have already earned their place in real enterprise work.</p>
<div class="abs products-btn"><span class="btn">Learn More</span></div>
<article class="abs product-card">
  <div class="pager"><span class="prev"></span><span class="next"></span></div>
  <h3>Orbit Relay</h3>
  <p>Orbit Relay is a simple tool that lets you add one short page to any app, where people can leave quick feedback about bugs or issues they are running into, so your team can act on real insight and keep every release running smoothly.</p>
  <div class="more">READ MORE →</div>
</article>

<!-- team -->
<h2 class="abs section-title team-title">Meet <span class="accent">The</span> Team</h2>
<p class="abs lead team-lead">At Byte Lantern Co. we don't just prescribe solutions for every business; we are a skilled team who build, test and support each product together.</p>
<div class="abs avatar" role="img" aria-label="Team member portrait" style="left:172px;top:2580px;width:80px;height:80px"></div>
<div class="abs avatar" role="img" aria-label="Team member portrait" style="left:348px;top:2620px;width:104px;height:104px"></div>
<div class="abs avatar" role="img" aria-label="Team member portrait" style="left:692px;top:2576px;width:72px;height:72px"></div>
<div class="abs avatar" role="img" aria-label="Team member portrait" style="left:960px;top:2604px;width:96px;height:96px"></div>
<div class="abs avatar" role="img" aria-label="Team member portrait" style="left:132px;top:2852px;width:96px;height:96px"></div>
<div class="abs avatar" role="img" aria-label="Team member portrait" style="left:360px;top:2836px;width:64px;height:64px"></div>
<div class="abs avatar" role="img" aria-label="Team member portrait" style="left:760px;top:2728px;width:64px;height:64px"></div>
<div class="abs avatar" role="img" aria-label="Team member portrait" style="left:956px;top:2848px;width:104px;height:104px"></div>
<div class="abs avatar main" role="img" aria-label="Portrait of featured team member Maren Ostwald" style="left:540px;top:2690px;width:160px;height:160px"></div>
<div class="abs member-name">Maren Ostwald</div>
<div class="abs member-role">Co-Founder</div>
<div class="abs member-social"><span></span><span class="on"></span><span></span></div>

<!-- case studies -->
<article class="abs case-card">
  <div class="pager"><span class="prev"></span><span class="next"></span></div>
  <h3>Self-Help &amp; Wellness</h3>
  <p>Our client is a self-help and wellness network marketing company ranked among the top sellers in its region. We rebuilt their ordering platform and connected every system, so thousands of active members now enjoy faster checkout and clear reporting.</p>
  <div class="more">READ MORE →</div>
</article>
<h2 class="abs case-title">Case <span class="accent">Studies</span></h2>
<p class="abs case-text">The following are snapshots of some of the work we've done for clients. By default, all our clients are kept private, so only cases cleared for publishing are shown here.</p>
<div class="abs case-btn"><span class="btn">Learn More</span></div>

<!-- call to action -->
<h2 class="abs cta-title"><span class="accent">READY TO</span> GET STARTED</h2>
<div class="abs cta-btn"><span class="btn">Get Started</span></div>

<!-- tech partners -->
<div class="abs tech-row" style="top:4008px">
  <div class="tech"><i></i>Quartzly</div>
  <div class="tech"><i></i>Hullbox</div>
  <div class="tech"><i></i>Tidebase</div>
  <div class="tech"><i></i>Burrowdb</div>
  <div class="tech"><i></i>Coilscript</div>
</div>
<div class="abs tech-row" style="top:4100px;left:430px;width:340px">
  <div class="tech"><i></i>Garnetic</div>
  <div class="tech">Tongueset</div>
</div>

<!-- footer -->
<footer class="abs footer"></footer>
<div class="abs footer-col" style="left:140px">
  <h4><span class="accent">Quick</span> Links</h4>
  <ul class="links"><li>Home</li><li>About</li><li>Services</li><li>Products</li><li>Team</li><li>Case Studies</li><li>Media</li><li>Contact</li></ul>
</div>
<div class="abs footer-col contact" style="left:360px;width:260px">
  <h4><span class="accent">Contact</span> Details</h4>
  <div class="brand">Byte Lantern Co.</div>
  <div class="row"><svg viewBox="0 0 14 14"><path d="M7 1a4 4 0 0 1 4 4c0 3-4 8-4 8S3 8 3 5a4 4 0 0 1 4-4Z" fill="#f15a24"/><circle cx="7" cy="5" r="1.5" fill="#fff"/></svg><span>140 Harbour Street, Lantern Quay 4021</span></div>
  <div class="row"><svg viewBox="0 0 14 14"><path d="M3 1h3l1 3-2 1a8 8 0 0 0 4 4l1-2 3 1v3c0 1-1 2-2 2A11 11 0 0 1 1 3c0-1 1-2 2-2Z" fill="#f15a24"/></svg><span>+1 (555) 018 2406</span></div>
  <div class="row"><svg viewBox="0 0 14 14"><rect x="1" y="3" width="12" height="8" rx="1" fill="#f15a24"/><path d="M1 4l6 4 6-4" stroke="#fff" fill="none"/></svg><span>hello@bytelantern.co</span></div>
</div>
<div class="abs footer-col inquiry" style="left:672px">
  <h4><span class="accent">Quick</span> Inquiry</h4>
  <div class="field">Name</div>
  <div class="field">Email</div>
  <div class="field">Phone</div>
  <div class="field tall">Message</div>
  <span class="btn" style="margin-top:6px">Send Now</span>
</div>
<div class="abs footer-col follow" style="left:960px">
  <h4><span class="accent">Follow</span> Us</h4>
  <ul><li><span></span>Friendwall</li><li><span></span>Chirpline</li><li><span></span>Worknet</li><li><span></span>Circleplus</li></ul>
</div>
<div class="abs copyright">Copyright © 2018 Byte Lantern Co. All Rights Reserved.</div>

</body>
</html>
```